Online Dating Ebook Needs an Amazing Cover Design

This is a cover for an online dating ebook that will go online to the Pagewell store and will have a large audience. It is targeted primarily to men and is written from the perspective of a Strategy Consultant

The cover needs to be elegant, seductive and eye catching but not overbearing or cheesy. No pornography, outright nudity, etc. It should draw the eye.

The title is

"Master Web Romance" with the subtitle "A Business Advisor's Handbook"

The author's name would need to be Mark Tellby.

Feel free to send emails asking for feedback on your designs so we can work on many versions

Target Market(s)

Target market is 18-40 year old single males who will be doing online dating

Industry/Entity Type

Dating

Requirements
Must have
• 1)Must be given a .jpg and vector file.

2) Must be 900 pixel Height and 600 pixel width.

3)Need a 300 dpi and 72 dpi version

4) Author's name as Mark Tellby

```html
<!DOCTYPE html>
<html lang="en">
<head>
<meta charset="utf-8">
<title>Master Web Romance — A Business Advisor's Handbook</title>
<link rel="stylesheet" href="https://fonts.googleapis.com/css2?family=Cinzel+Decorative:wght@400&family=Fjalla+One&family=Jost:wght@400&display=swap">
<style>
  :root {
    --cover-grey: #bdbdbd;
    --title-blue: #0f9ad9;
    --title-black: #231f1c;
    --title-pink: #ec1b8c;
    --subtitle-white: #fdf1f4;
    --author-ink: #1f1f1f;
    --love-blue: #0b93d6;
    --love-violet: #8d6fb5;
    --love-magenta: #e5148a;
    --love-orange: #f07f22;
    --love-yellow: #fcc713;
    --love-lime: #9fcb3c;
    --love-green: #0aa64a;
  }
  html, body {
    margin: 0;
    padding: 0;
    width: 800px;
    height: 1200px;
    overflow: hidden;
    background: var(--cover-grey);
  }
  .cover {
    position: relative;
    width: 800px;
    height: 1200px;
    background: var(--cover-grey);
    overflow: hidden;
  }
  .title {
    position: absolute;
    left: 44px;
    top: 0;
    margin: 0;
    font-family: "Cinzel Decorative", serif;
    font-weight: 400;
    font-size: 118px;
    line-height: 160px;
    letter-spacing: 1px;
  }
  .title span { display: block; white-space: nowrap; }
  .title .line-one { color: var(--title-blue); }
  .title .line-two { color: var(--title-black); }
  .title .line-three { color: var(--title-pink); }
  .love-art {
    position: absolute;
    left: 76px;
    top: 462px;
    width: 600px;
    height: 456px;
  }
  .subtitle {
    position: absolute;
    left: 24px;
    top: 1010px;
    margin: 0;
    font-family: "Fjalla One", sans-serif;
    font-weight: 400;
    font-size: 44px;
    color: var(--subtitle-white);
    letter-spacing: 0.5px;
    white-space: nowrap;
  }
  .author {
    position: absolute;
    left: 483px;
    top: 1138px;
    margin: 0;
    font-family: "Jost", sans-serif;
    font-weight: 400;
    font-size: 44px;
    color: var(--author-ink);
    white-space: nowrap;
  }
</style>
</head>
<body>
<main class="cover">
  <h1 class="title">
    <span class="line-one">MASTER</span>
    <span class="line-two">WEB</span>
    <span class="line-three">ROMANCE</span>
  </h1>

  <svg class="love-art" viewBox="0 0 600 456" role="img" aria-label="Large multicoloured word LOVE with a silhouette of a woman sitting on top and a silhouette of a man leaning against the right side">
    <defs>
      <linearGradient id="love-spectrum" x1="0" y1="0" x2="1" y2="0">
        <stop offset="0" stop-color="var(--love-blue)"/>
        <stop offset="0.18" stop-color="var(--love-violet)"/>
        <stop offset="0.36" stop-color="var(--love-magenta)"/>
        <stop offset="0.54" stop-color="var(--love-orange)"/>
        <stop offset="0.66" stop-color="var(--love-yellow)"/>
        <stop offset="0.8" stop-color="var(--love-lime)"/>
        <stop offset="1" stop-color="var(--love-green)"/>
      </linearGradient>
    </defs>
    <rect x="0" y="145" width="560" height="305" rx="8" fill="url(#love-spectrum)" opacity="0.9"/>
  </svg>

  <p class="subtitle">A Business Advisor's Handbook</p>
  <p class="author">Mark Tellby</p>
</main>
</body>
</html>
```